Flyer design for Trail Beside Outback Trips

We need a new flyer for our tour business. Sketch hive produced a great flyer for us 4 years ago but it is time to update. We have had a price increase that needs to be reflected but we have noticed an issue with our current marketing.
Our tour is a "tagalong" tour which means you follow in your own vehicle. Unfortunately most people associate "tagalong" with 4wd (Four wheel drive vehicles). This is not the case for our tour which can be done in ANY type of vehicle. We need to get across at first glance that this tour is available to all vehicle types. We also need to stress that there is NOT MUCH DRIVING. We cover around 20km total of very easy driving. We go from point of interest to point of interest.
We want our customers to feel that this tour will be a better option than selecting a bus type tour because they use their own vehicle. Our option is also MUCH cheaper than bus options but provides a premium product. It's "cheap" but not cheap if you understand.
I will upload our previous flyer so you have an idea of what we do and how we have been presenting it. We are currently single sided DL but do not mind if we go into double sided DL if you feel that will enable you to share more information. Our price is $50 and half price for kids (as per old flyer)
Some things to remember when trying to appeal to our customer:
Choose a design that clearly communicates that our tagalong tour is suitable for all types of vehicles. For example, "Vehicle-Friendly Tagalong Tour" or "All-Vehicle Tagalong Tour".
Use clear language: Avoid using terms like "off-road" or "4x4" that may imply that our tour is only suitable for certain types of vehicles. Instead, use language that is inclusive and clearly communicates that all vehicles are welcome.
Include photos and videos of a variety of vehicles: This will show potential customers that our tagalong tour is not limited to four-wheel drive vehicles and that any type of vehicle can participate.
Highlight the benefits of a tagalong tour over a bus tour: Emphasise the flexibility and freedom that a tagalong tour offers, as well as the opportunity to explore off-the-beaten-path destinations that are not accessible by bus.
By incorporating these elements into your product presentation, you can avoid confusion and clearly communicate that our tagalong tour is suitable for any type of vehicle, while also highlighting the unique benefits of this type of tour.
Along with the emphasis on all vehicles you need to be clear about what we offer on the tour.
- The excitement of an opal mine tour with an award winning guide and opal miner.
- The wonder of an underground home and discovering how people live in an underground environment.
- Driving through the opal mining area for a close up view of the field.
- Our EXCLUSIVE opal cutting and polishing demonstration.
- The adventure of looking for your own opal.
For further information visit our web site "http://trailbeside.outbackway.example". Check our facebook page "https://www.facebook.com/trailbesideoutbacktrips". Search Seekora for "Coober Pedy", Trail beside Outback Coober Pedy" or "Coober Pedy Opal mining" to source images of our town and opals.
PLEASE ALSO FIND SOMEWHERE TO SAY "FREE UNPOWERED CAMPING AT TALMO'S WITH ALL TOURS AS WELL AS DISCOUNTS ON POWERED CAMPING" and make this stand out somehow. (http://stay-belowgrid.example.au)

Target Market(s)

18 to 80

Industry/Entity Type

Tourism

Font styles to use
Serif

Colors

Designer to choose colors to be used in the design.

Requirements
Must have
• Eye catching images and attention grabbing headlines
Nice to have
• Modern design.
Should not have
• References to 4wd or buses.

```html
<!DOCTYPE html>
<html lang="en">
<head>
<meta charset="utf-8">
<title>Trail Beside Outback Trips – Flyer</title>
<link href="https://fonts.googleapis.com/css2?family=Roboto+Slab:wght@400;500;700;800&display=swap" rel="stylesheet">
<style>
  :root {
    --orange: #f08424;
    --ink: #111111;
    --grey: #555555;
    --paper: #ffffff;
    --backdrop: #eeeeee;
    --sky: #c9cdd0;
    --earth: #b8714a;
    --scrub: #8d8a5c;
  }
  * { margin: 0; padding: 0; box-sizing: border-box; }
  html, body { width: 1200px; height: 1200px; overflow: hidden; }
  body { background: var(--backdrop); font-family: 'Roboto Slab', serif; position: relative; }

  .flyer {
    position: absolute; left: 343px; top: 56px; width: 513px; height: 1088px;
    background: var(--paper); overflow: hidden;
  }
  .abs { position: absolute; }

  .brand-mark {
    left: 29px; top: 22px; width: 150px; height: 150px; border-radius: 50%;
    background: var(--orange); display: flex; align-items: center; justify-content: center;
    text-align: center; color: var(--paper); font-weight: 500; font-size: 17px; line-height: 1.25;
  }

  .social { left: 383px; top: 25px; display: flex; gap: 10px; }
  .social span { width: 27px; height: 27px; border-radius: 5px; background: var(--orange); display: block; }
  .email { right: 18px; top: 55px; font-size: 10.5px; color: var(--grey); }

  .price-badge {
    left: 335px; top: 87px; width: 174px; height: 174px; border-radius: 50%;
    background: var(--orange); color: var(--paper); text-align: center;
  }
  .price-badge::before {
    content: ""; position: absolute; inset: 5px; border-radius: 50%;
    border: 4px dotted var(--paper);
  }
  .price-amount { position: absolute; left: 0; right: 0; top: 20px; font-weight: 800; font-size: 50px; line-height: 1; }
  .price-amount small { font-size: 20px; font-weight: 700; vertical-align: 4px; margin-right: 2px; }
  .price-unit { position: absolute; left: 0; right: 0; top: 78px; font-weight: 700; font-size: 18px; }
  .price-note { position: absolute; left: 0; right: 0; top: 104px; font-size: 9px; font-weight: 500; line-height: 1.2; }

  .title-small { left: 28px; top: 200px; font-size: 23px; font-weight: 500; color: var(--ink); }
  .title-box {
    left: 29px; top: 233px; width: 294px; height: 47px; background: var(--orange);
    color: var(--paper); font-weight: 700; font-size: 34px; line-height: 47px; padding-left: 12px;
  }

  .photo-scene {
    left: 0; top: 350px; width: 513px; height: 300px;
    background: linear-gradient(180deg, #ffffff 0%, var(--sky) 16%, #d8d8d2 26%, var(--scrub) 32%, var(--earth) 52%, #c88a62 78%, #ffffff 100%);
  }
  .headline { left: 29px; top: 302px; font-weight: 700; font-size: 30px; color: var(--orange); line-height: 1.2; }
  .subline { left: 29px; top: 340px; font-size: 15px; color: var(--grey); }

  .vehicle-tag {
    left: 0; top: 436px; padding: 7px 14px 7px 29px; background: var(--orange);
    color: var(--paper); border-radius: 0 20px 20px 0; line-height: 1.3;
  }
  .vehicle-tag strong { display: block; font-size: 15px; font-weight: 800; }
  .vehicle-tag span { display: block; font-size: 11.5px; font-weight: 500; }

  .photo-round {
    left: 305px; top: 403px; width: 224px; height: 224px; border-radius: 50%;
    border: 7px solid var(--orange);
    background: linear-gradient(180deg, #a9b6bd 0%, #b7c0c3 50%, #9c8f80 70%, #8a5a3a 100%);
  }

  .section-pill {
    left: 0; top: 571px; width: 256px; height: 56px; background: rgba(255,255,255,0.92);
    border-radius: 0 28px 28px 0; color: var(--orange); font-weight: 800; font-size: 34px;
    line-height: 56px; padding-left: 28px;
  }

  .intro { left: 22px; top: 642px; width: 480px; font-size: 11.8px; line-height: 18.5px; color: var(--grey); white-space: nowrap; }
  .intro b { font-weight: 700; color: var(--ink); }

  .offer-title { left: 30px; top: 719px; font-weight: 700; font-size: 19px; color: var(--orange); }
  .offer-item { left: 30px; font-size: 15.5px; line-height: 18.6px; color: var(--grey); padding-left: 15px; white-space: nowrap; }
  .offer-item::before {
    content: ""; position: absolute; left: 0; top: 5px; width: 9px; height: 9px;
    border-radius: 50%; background: var(--orange);
  }

  .book-now { left: 300px; top: 885px; font-weight: 800; font-size: 27px; color: var(--orange); }
  .phone-pill {
    left: 276px; top: 921px; width: 222px; height: 39px; border-radius: 8px; background: var(--orange);
    color: var(--paper); font-weight: 700; font-size: 20px; display: flex; align-items: center; justify-content: center; gap: 6px;
  }

  .camping-callout {
    left: 22px; top: 984px; width: 469px; height: 60px; border-radius: 8px;
    background: var(--orange); color: var(--paper); text-align: center; padding-top: 9px;
  }
  .camping-callout strong { display: block; font-size: 16px; font-weight: 800; line-height: 1.3; }
  .camping-callout span { display: block; font-size: 12px; font-weight: 500; line-height: 1.4; }

  .footer-line { top: 1067px; height: 2px; background: var(--orange); }
  .footer-url { left: 0; right: 0; top: 1058px; text-align: center; font-size: 12px; color: var(--grey); }
  .footer-url b { font-weight: 700; }
</style>
</head>
<body>
<main class="flyer">
  <div class="abs brand-mark">Trail Beside<br>Outback</div>

  <div class="abs social"><span></span><span></span></div>
  <div class="abs email">hello@trailbeside.example</div>

  <div class="abs title-small">TRAIL BESIDE</div>
  <div class="abs title-box">OUTBACK</div>

  <div class="abs photo-scene" role="img" aria-label="Wide view over the Coober Pedy township with red earth, scrub and everyday cars on easy sealed roads"></div>
  <div class="abs headline">ARE YOU READY</div>
  <div class="abs subline">TO GO DOWN UNDER... DOWN UNDER?</div>

  <div class="abs vehicle-tag">
    <strong>ALL-VEHICLE TAGALONG TOUR</strong>
    <span>ANY CAR WELCOME · ONLY ~20 KM EASY DRIVING</span>
  </div>

  <div class="abs price-badge">
    <div class="price-amount"><small>$</small>50</div>
    <div class="price-unit">PER PERSON</div>
    <div class="price-note">(KIDS HALF PRICE AND<br>CHILDREN UNDER <b>5 FREE!</b>)</div>
  </div>

  <div class="abs photo-round" role="img" aria-label="Old rusty truck and opal mining blower beside mullock heaps"></div>

  <div class="abs section-pill">THE TOUR</div>

  <p class="abs intro"><b>ALL-VEHICLE</b> TAGALONG TOUR OF COOBER PEDY – ANY CAR,<br>VAN OR CARAVAN WELCOME. ONLY ABOUT 20 KM OF VERY EASY<br>DRIVING, STOP TO STOP, AS OUR GUIDE SHOWS YOU A "DAY IN<br>THE LIFE" OF A MINER. YOUR CAR, YOUR PACE, PREMIUM GUIDING.</p>

  <h2 class="abs offer-title">WHAT'S ON THE TOUR?</h2>
  <div class="abs offer-item" style="top:757px">LIFE IN A REAL UNDERGROUND HOME</div>
  <div class="abs offer-item" style="top:782px">OPAL MINE TOUR WITH AN AWARD-WINNING<br>GUIDE AND WORKING OPAL MINER</div>
  <div class="abs offer-item" style="top:826px">CLOSE-UP DRIVE THROUGH THE OPAL FIELDS</div>
  <div class="abs offer-item" style="top:851px">OUR EXCLUSIVE OPAL CUTTING AND<br>POLISHING DEMONSTRATION</div>
  <div class="abs offer-item" style="top:894px">FIND YOUR OWN OPAL</div>
  <div class="abs offer-item" style="top:920px">YOUR CAR, YOUR<br>PACE – NO BIG<br>CROWDS</div>

  <div class="abs book-now">BOOK NOW!</div>
  <div class="abs phone-pill">
    <svg width="18" height="18" viewBox="0 0 24 24" aria-hidden="true">
      <circle cx="12" cy="12" r="11" fill="#ffffff"/>
      <path d="M8.2 6.5c.4-.4 1-.4 1.3 0l1.3 1.7c.3.4.3.9-.1 1.3l-.8.8c.6 1.3 1.6 2.3 2.9 2.9l.8-.8c.4-.4.9-.4 1.3-.1l1.7 1.3c.4.3.4.9 0 1.3l-.9.9c-.6.6-1.5.8-2.3.5-3-1.1-5.4-3.5-6.5-6.5-.3-.8-.1-1.7.5-2.3z" fill="#f08424"/>
    </svg>
    (08) 5550 1427
  </div>

  <div class="abs camping-callout">
    <strong>FREE UNPOWERED CAMPING AT TALMO'S</strong>
    <span>WITH ALL TOURS + DISCOUNTS ON POWERED CAMPING</span>
  </div>

  <div class="abs footer-line" style="left:9px;width:112px"></div>
  <div class="abs footer-url">www.<b>trailbeside.outbackway</b>.example</div>
  <div class="abs footer-line" style="right:9px;width:112px"></div>
</main>
</body>
</html>
```